Flyer-Design für Immobilienmarketing von Raumfreude Home Staging
Zielgruppe
Wir (Raumfreude Home Staging) geben mit Home Staging Immobilien ein Raumfreude (www.raumfreude-beispiel.de). Ziel ist die Immobilienvermarktung zu beschleunigen (Immobilienmarketing) und den besten Preis zu erzielen. Durch ein eigenes Möbel und Dekolager erfolgt die Gestaltung zeitnah.
Zielgruppe sind Immobilienverkäufer (privat) und auch Makler/Vermittler/Projektentwickler
Aufgabenstellung
Wir benötigen einen Flyer/Klappkarte DIN lang quer. Dieser sollte hochwertig, einladend, hell und freundlich erscheinen. Wenn er an der langen Seite gefaltet ist, sollte er als Klappkarte auf dem Tisch stehen können. Dabei sollen alle 4 Seiten genutzt werden. Logo und Design sowie Kurzbeschreibungen/Texte entsprechend bitte der Website (www.raumfreude-beispiel.de) verwenden. Originale können zur Verfügung gestellt werden. Der Flyer sollte auch als PDF nutzbar sein.
Als Slogan stellen wir uns folgendes vor 'Mit Raumfreude in den Immobilienverkauf starten und beim besten Preis landen', sind aber für alles offen. Bei Verwendung von Referenzen wäre ein Spruch mit 'Wohlfühlen' gut. Des Weiteren einfach bei den Texten und Bildern der Website bedienen (Vorteile + warum mit uns) und einen knackigen überzeugenden Flyer bei dem hauptsächlich die Bilder sprechen, erstellen. Wir freuen uns auf die Vorschläge.

```html
<!DOCTYPE html>
<html lang="de">
<head>
<meta charset="utf-8">
<title>Raumfreude Home Staging – Flyer</title>
<link href="https://fonts.googleapis.com/css2?family=Roboto:wght@300;400&display=swap" rel="stylesheet">
<style>
  :root {
    --green: #99c11c;
    --text: #3c3c3c;
    --rule: #8a8a8a;
    --white: #ffffff;
    --photo-light: #e9ebe6;
    --photo-mid: #c9d3c0;
  }
  * { margin: 0; padding: 0; box-sizing: border-box; }
  html, body { width: 1200px; height: 1143px; overflow: hidden; background: var(--white); }
  body { font-family: 'Roboto', Arial, sans-serif; color: var(--text); position: relative; }

  .headline {
    position: absolute; left: 57px; top: 36px;
    font-weight: 400; font-size: 29px; line-height: 36px; letter-spacing: 0.6px;
    color: var(--green); text-transform: uppercase;
  }
  .intro-line { position: absolute; left: 57px; top: 114px; font-size: 18.5px; font-weight: 400; }

  .feature { position: absolute; width: 330px; }
  .feature h3 { font-weight: 400; font-size: 19px; line-height: 26px; color: var(--green); }
  .feature p { font-size: 18.5px; line-height: 26px; }

  .hero-photo {
    position: absolute; left: 777px; top: 163px; width: 371px; height: 328px;
    background: linear-gradient(160deg, var(--photo-light) 0%, #dfe5d8 45%, var(--photo-mid) 100%);
  }
  .hero-bar { position: absolute; left: 777px; top: 491px; width: 371px; height: 23px; background: var(--green); }

  .divider { position: absolute; left: 0; top: 571px; width: 1200px; height: 1px; background: var(--rule); }

  .quote-badge { position: absolute; left: 34px; top: 646px; width: 386px; height: 386px; }
  .quote-text {
    position: absolute; left: 34px; top: 704px; width: 386px;
    text-align: center; color: var(--white); font-weight: 300; font-size: 35px; line-height: 47px;
  }

  .benefits-title { position: absolute; left: 452px; top: 600px; font-weight: 400; font-size: 28px; color: var(--green); }
  .benefits-intro { position: absolute; left: 452px; top: 634px; font-size: 18.5px; line-height: 27px; }

  .benefit { position: absolute; width: 345px; }
  .benefit h3 { font-weight: 400; font-size: 19px; line-height: 26px; color: var(--green); }
  .benefit p { font-size: 18.5px; line-height: 24.5px; }

  .footer-band { position: absolute; left: 0; top: 1115px; width: 1200px; height: 28px; background: var(--green); }
</style>
</head>
<body>
  <h1 class="headline">Mit Raumfreude in den Immobilienverkauf starten<br>und beim besten Preis landen.</h1>
  <p class="intro-line">Warum mit uns? Das erwartet Sie bei Raumfreude HomeStaging:</p>

  <div class="feature" style="left:57px; top:167px;">
    <h3>Ganzheitliches Konzept</h3>
    <p>Mit unserem Einrichtungs- und Farbkonzept erhält jeder Raum seine Funktion mit einer einladenden und harmonischen Möblierung - für ein Hier-will-ich-wohnen-Gefühl.</p>
  </div>
  <div class="feature" style="left:412px; top:167px;">
    <h3>Schnelle Umsetzung</h3>
    <p>Mit unserem eigenen Möbellager richten wir Immobilien schnell, individuell und komplett ein - für einen schnellen Start in die Immobilienvermarktung.</p>
  </div>
  <div class="feature" style="left:57px; top:355px;">
    <h3>Alles aus einer Hand</h3>
    <p>Unser Team kümmert sich vom Konzept, über die Umsetzung bis zur Betreuung während der Vermarktung um die Immobilie - für den perfekten ersten Eindruck.</p>
  </div>
  <div class="feature" style="left:412px; top:353px;">
    <h3>Erfahrung und Erfolge</h3>
    <p>Wir wissen, was bei Käufern gut ankommt. Unsere gesammelten Erfahrungen setzen wir gezielt ein, damit sich jede Immobilie schnell und zum besten Preis verkauft.</p>
  </div>

  <div class="hero-photo" role="img" aria-label="Foto eines hellen, mit Sesseln und Beistelltisch eingerichteten Wohnraums vor großem Fenster"></div>
  <div class="hero-bar"></div>

  <div class="divider"></div>

  <svg class="quote-badge" viewBox="0 0 386 386" aria-hidden="true">
    <circle cx="193" cy="193" r="193" fill="#99c11c"/>
    <circle cx="193" cy="193" r="176" fill="none" stroke="#ffffff" stroke-width="1.2" stroke-dasharray="520 70 400 116" transform="rotate(-110 193 193)"/>
    <g fill="#ffffff">
      <path d="M55 70 h12 l-4 34 h-10 z M73 70 h12 l-4 34 h-10 z"/>
      <path d="M296 304 h12 l-4 34 h-10 z M314 304 h12 l-4 34 h-10 z"/>
    </g>
  </svg>
  <p class="quote-text">Hier fühlte<br>ich mich gleich<br>wie Zuhause und<br>wollte sofort<br>die Wohnung<br>kaufen.</p>

  <h2 class="benefits-title">Ihre Vorteile</h2>
  <p class="benefits-intro">Wir machen den Wert und das Potential Ihrer Immobilie für Käufer sichtbar.<br>Profitieren Sie von den Vorteilen mit einem Raumfreude Home Staging.</p>

  <div class="benefit" style="left:455px; top:704px;">
    <h3>Sie wecken das größte Interesse</h3>
    <p>Wir setzen Ihre Immobilie mit den passenden Möbeln für den Verkauf gekonnt in Szene und wecken mit professionellen Immobilienfotos das größte Kaufinteresse.</p>
  </div>
  <div class="benefit" style="left:826px; top:704px; width:330px;">
    <h3>Sie erzielen den besten Preis</h3>
    <p style="line-height:26px;">Mit unserem hochwertigen Home Staging machen wir den Wert Ihrer Immobilie sichtbar und zeigen das Potential auf. So erzielen Sie den besten Preis.</p>
  </div>
  <div class="benefit" style="left:459px; top:900px;">
    <h3>Sie sparen viel Zeit und Nerven</h3>
    <p style="line-height:26px;">Unser Ziel ist eine kurze Vermarktungszeit Ihrer Immobilie. Damit sparen Sie die weiteren laufenden Kosten der Immobilie und verringern die Anzahl der Besichtigungen.</p>
  </div>
  <div class="benefit" style="left:826px; top:900px; width:330px;">
    <h3>Sie finden schnell einen Käufer</h3>
    <p>Kaufinteressenten wollen sich in ihr zukünftiges Zuhause sofort verlieben. Mit unserem Raumfreude fällt die Entscheidung für Ihre Immobilie ganz leicht und schnell.</p>
  </div>

  <div class="footer-band"></div>
</body>
</html>
```